Text only wordpress site to capture emails

Refer to inspiration upload for list of sites that will be useful for you.

We need a site that will be used to capture emails from clients that follow us on social media. The site will be all text, pretty simple. I have a couple of text sites that I like and we can use them for an example.

Menu section will have home, archive, about.
Footer will have © and Website Privacy Policy | Legal and Policies
There will be some text on the home page and an email capture.

This site will be all text no pictures.

I discuss office politics so the text portions will have some questions and answers on this and then prompt for the visitor to subscribe to my email list.

The only purpose of the site is to build an email list from existing social media followers so the site will be pretty simple in and of itself.

• Text only, similar Q&A to uploaded pics.

I will use a template from mail lantern dotcom for email capture.

I like the simple couriernew font family that is on both sites supplied in the uploads.
• If you use any color it needs to be very minimal.

```html
<!DOCTYPE html>
<html lang="en">
<head>
<meta charset="utf-8">
<title>Your Site</title>
<link rel="stylesheet" href="https://fonts.googleapis.com/css2?family=Courier+Prime:wght@400;700&display=swap">
<style>
  :root {
    --ink: #000000;
    --paper: #ffffff;
    --text: #222222;
    --muted-button: #2b2b2b;
    --light: #ffffff;
  }
  * { box-sizing: border-box; margin: 0; padding: 0; }
  html, body {
    width: 1200px;
    height: 996px;
    overflow: hidden;
    background: var(--paper);
    font-family: "Courier Prime", "Courier New", monospace;
    color: var(--text);
  }
  .site-header {
    height: 230px;
    background: var(--ink);
    color: var(--light);
    position: relative;
  }
  .top-bar {
    display: flex;
    justify-content: space-between;
    align-items: center;
    padding: 16px 92px 0 180px;
    height: 42px;
  }
  .brand {
    font-weight: 700;
    font-size: 19px;
    letter-spacing: 0.5px;
  }
  .main-nav {
    display: flex;
    gap: 14px;
  }
  .main-nav a {
    color: var(--light);
    text-decoration: none;
    font-weight: 700;
    font-size: 13px;
  }
  .hero {
    text-align: center;
    padding-top: 38px;
  }
  .hero-title {
    font-size: 44px;
    font-weight: 700;
    line-height: 1;
    letter-spacing: 1px;
  }
  .hero-tagline {
    margin-top: 28px;
    font-size: 18px;
    font-weight: 700;
  }
  .faq {
    height: 638px;
    padding: 80px 100px 0 110px;
  }
  .faq-item {
    margin-bottom: 17px;
    font-size: 15.5px;
    line-height: 25px;
    letter-spacing: 1.2px;
    max-width: 1000px;
  }
  .faq-question {
    text-decoration: underline;
    text-underline-offset: 3px;
  }
  .site-footer {
    height: 128px;
    background: var(--ink);
    color: var(--light);
    text-align: center;
    font-weight: 700;
    font-size: 14px;
    letter-spacing: 0.8px;
    padding-top: 46px;
    position: relative;
  }
  .footer-link { display: block; color: var(--light); text-decoration: none; }
  .copyright { margin-top: 24px; }
  .back-to-top {
    position: absolute;
    right: 3px;
    bottom: 4px;
    width: 31px;
    height: 31px;
    border-radius: 3px;
    background: var(--muted-button);
    display: flex;
    align-items: center;
    justify-content: center;
  }
</style>
</head>
<body>
  <header class="site-header">
    <div class="top-bar">
      <span class="brand">Your Site</span>
      <nav class="main-nav">
        <a href="#">Home</a>
        <a href="#">About</a>
        <a href="#">Archive</a>
      </nav>
    </div>
    <div class="hero">
      <h1 class="hero-title">Your Site</h1>
      <p class="hero-tagline">Fusce pharetra imperdiet tempor.</p>
    </div>
  </header>

  <main class="faq">
    <div class="faq-item">
      <p class="faq-question">Q: What is Lorem Ipsum?</p>
      <p class="faq-answer">A: Lorem ipsum dolor sit amet, consectetur adipiscing elit. Vivamus ac dignissim diam. Vestibulum ante ipsum primis in faucibus orci luctus et ultrices posuere cubilia curae.</p>
    </div>
    <div class="faq-item">
      <p class="faq-question">Q: Why do we use it?</p>
      <p class="faq-answer">A : Nulla dui purus, congue eget magna ornare, aliquet pharetra tellus. Etiam congue lectus est, at convallis metus vestibulum et. Mauris in ante ut eros mollis fermentum.</p>
    </div>
    <div class="faq-item">
      <p class="faq-question">Q: Where does it come from?</p>
      <p class="faq-answer">A: Sed non erat venenatis, pretium nibh a, semper augue. Nulla volutpat rhoncus ullamcorper. Nulla varius nunc sed dui euismod, non scelerisque ligula sagittis.</p>
    </div>
    <div class="faq-item">
      <p class="faq-question">Q: Where can I get some?</p>
      <p class="faq-answer">A: Fusce pharetra imperdiet tempor. Proin in augue vel mi mattis tincidunt eu id neque. Aliquam sed diam eget ipsum malesuada aliquam sed eu purus. Morbi dictum finibus convallis.</p>
    </div>
    <div class="faq-item">
      <p class="faq-question">Q: How do i subscribe?</p>
      <p class="faq-answer">A: Nunc accumsan posuere ullamcorper. Nam eleifend eros tellus, sit amet luctus ipsum consequat et. Sed at porta dui, sit amet tincidunt odio. Vestibulum vestibulum congue ligula, in tempor neque facilisis non. Nullam faucibus accumsan semper.</p>
    </div>
  </main>

  <footer class="site-footer">
    <a class="footer-link" href="#">Privacy Policy</a>
    <p class="copyright">©2021 Your Site</p>
    <a class="back-to-top" href="#" aria-label="Back to top">
      <svg width="14" height="14" viewBox="0 0 14 14" aria-hidden="true">
        <path d="M7 13V2M2 6.5L7 1.5l5 5" fill="none" stroke="#ffffff" stroke-width="2.2" stroke-linecap="round" stroke-linejoin="round"/>
      </svg>
    </a>
  </footer>
</body>
</html>
```